Baby acupressure app for parents

We need an app for parents that teaches parents how to help them relieve their baby's imbalances (stomach ache, trouble sleeping etc.)

Please see the attached document (with info) and wireframes.

This project is urgent so please only participate if you're able to finish all screens within a few days after the contest is over.

Target Market(s)

Baby moms (20-40 years of age)

Industry/Entity Type

Baby Care

Colors
886aae
b768aa
e667a6
f68d4d
faa54b
fac994
f9ba93
f59195
fee18a

Requirements
Must have
• A high quality design that is both modern and very sleek and stylish.
Nice to have
• Simple animations to make the app "feel" like it's extreme high quality and make the user want to use it again and again
Should not have
• Sandwich menus

```html
<!DOCTYPE html>
<html lang="en">
<head>
<meta charset="utf-8">
<title>Tella Rest – app screens</title>
<link href="https://fonts.googleapis.com/css2?family=Roboto+Condensed:wght@300;400;700&display=swap" rel="stylesheet">
<style>
  :root{
    --stage:#ececec;
    --plum-dark:#5e1a44;
    --plum:#8a3a6c;
    --mauve:#9c6a86;
    --dusk:#6e6478;
    --lavender:#886aae;
    --orchid:#b768aa;
    --pink:#e667a6;
    --orange:#f68d4d;
    --amber:#faa54b;
    --peach:#fac994;
    --ink:#141414;
    --white:#ffffff;
    --soft-white:rgba(255,255,255,.82);
    --bar:rgba(120,40,90,.55);
  }
  *{box-sizing:border-box;margin:0;padding:0}
  html,body{width:1200px;height:676px;overflow:hidden;background:var(--stage);font-family:"Roboto Condensed",sans-serif;color:var(--white)}
  .stage{position:relative;width:1200px;height:676px;display:flex;gap:22px;justify-content:center;align-items:center}
  .screen{position:relative;width:212px;height:377px;border-radius:6px;overflow:hidden;
    background:linear-gradient(180deg,var(--dusk) 0%,var(--mauve) 30%,var(--plum) 62%,var(--plum-dark) 100%);
    box-shadow:0 8px 24px rgba(0,0,0,.18)}
  .screen--onboard{background:linear-gradient(180deg,#7f8aa8 0%,#9b6c84 35%,#a0466e 70%,var(--plum-dark) 100%)}
  .screen--picker{background:linear-gradient(180deg,#8d6c8e 0%,#8f8fbf 25%,var(--orchid) 55%,var(--plum) 100%)}

  .brand{position:absolute;left:0;right:0;text-align:center;display:flex;flex-direction:column;align-items:center;gap:8px}
  .brand__dot{width:46px;height:46px;border-radius:50%;background:var(--white)}
  .brand__name{font-weight:700;font-size:15px;color:var(--white)}
  .splash .brand{top:150px}
  .onboard .brand{top:50px}
  .tagline{font-size:10px;color:var(--soft-white);font-weight:300}
  .btn-begin{position:absolute;top:205px;left:50%;transform:translateX(-50%);background:#1b1416;border:1.5px solid var(--amber);
    color:var(--amber);font-weight:300;font-size:20px;padding:3px 14px;border-radius:6px}
  .dots{position:absolute;top:318px;left:0;right:0;display:flex;justify-content:center;gap:8px}
  .dots span{width:4px;height:4px;border-radius:50%;background:rgba(255,255,255,.5)}
  .dots span.is-active{background:var(--white)}
  .disclaimer{position:absolute;bottom:12px;left:14px;right:14px;text-align:center;font-size:9px;font-style:italic;color:var(--soft-white);line-height:1.3}

  .hero{position:absolute;top:0;left:0;right:0;height:150px;border-radius:0 0 50% 50% / 0 0 26% 26%;
    background:linear-gradient(135deg,#a87a5e 0%,#c89a80 45%,#8a6f5f 100%)}
  .hero__play{position:absolute;left:88px;top:52px}
  .title{position:absolute;top:160px;left:0;right:0;text-align:center;font-weight:700;font-size:26px}
  .rule{position:absolute;top:198px;left:40px;right:40px;height:1px;background:rgba(255,255,255,.55)}
  .body{position:absolute;top:208px;left:22px;right:22px;text-align:center;font-size:9.5px;line-height:1.35;color:var(--soft-white)}

  .tabbar{position:absolute;bottom:0;left:0;right:0;height:52px;background:var(--bar);display:flex;justify-content:space-around;align-items:center;padding-top:4px}
  .tab{display:flex;flex-direction:column;align-items:center;gap:3px;font-size:7px}
  .tab svg{width:22px;height:20px}
  .tab.is-active::after{content:"";width:22px;height:1.5px;background:var(--orange)}

  .picker__title{position:absolute;top:14px;left:0;right:0;text-align:center;font-weight:700;font-size:26px}
  .picker__rule{position:absolute;top:50px;left:50px;right:50px;height:1px;background:rgba(255,255,255,.6)}
  .picker__intro{position:absolute;top:62px;left:30px;right:30px;text-align:center;font-size:9px;line-height:1.3;color:var(--soft-white)}
  .picker__cta{position:absolute;top:96px;left:0;right:0;text-align:center;font-size:10px;font-weight:700}
  .spots{position:absolute;top:118px;left:14px;right:14px;display:grid;grid-template-columns:1fr 1fr;gap:6px}
  .spot{position:relative;height:96px;border-radius:12px;overflow:hidden}
  .spot span{position:absolute;font-size:10px;font-weight:700}
  .spot--feet{background:linear-gradient(135deg,#e3c1b5,#c99d92)} .spot--feet span{top:6px;right:10px}
  .spot--hands{background:linear-gradient(135deg,#d8b09a,#b98d78)} .spot--hands span{top:6px;left:10px}
  .spot--face{background:linear-gradient(135deg,#e6d6d2,#c5b8c8)} .spot--face span{bottom:6px;right:10px}
  .spot--body{background:linear-gradient(135deg,#6b4a60,#4a3344)} .spot--body span{bottom:6px;left:10px;color:rgba(255,255,255,.6)}
  .lock{position:absolute;top:6px;right:8px;width:16px;height:16px;border-radius:50%;background:#2a1a24;display:flex;align-items:center;justify-content:center}
  .spot-center{position:absolute;top:176px;left:50%;transform:translateX(-50%);width:62px;height:62px;border-radius:50%;background:var(--ink);
    display:flex;align-items:center;justify-content:center;font-size:10px;font-weight:700}
</style>
</head>
<body>
<main class="stage">

  <section class="screen splash">
    <div class="brand"><span class="brand__dot"></span><span class="brand__name">Tella Rest</span></div>
  </section>

  <section class="screen screen--onboard onboard">
    <div class="brand"><span class="brand__dot"></span><span class="brand__name">Tella Rest</span><span class="tagline">Help relieve your child balance</span></div>
    <div class="btn-begin">Begin</div>
    <div class="dots"><span></span><span></span><span class="is-active"></span></div>
    <p class="disclaimer">Always consult a physician if you suspect your child is in need of health care. See FAQ for more info.</p>
  </section>

  <section class="screen home">
    <div class="hero" role="img" aria-label="Video still of a smiling instructor, with a play button"></div>
    <svg class="hero__play" width="36" height="40" viewBox="0 0 36 40"><path d="M4 4 L32 20 L4 36 Z" fill="none" stroke="var(--orange)" stroke-width="3" stroke-linejoin="round"/></svg>
    <h1 class="title">Tella Rest</h1>
    <div class="rule"></div>
    <p class="body">Lorem ipsum dolor sit amet, consectetur adipiscing elit, sed do eiusmod tempor incididunt ut labore et dolore magna aliqua. Ut enim ad minim veniam. Lorem ipsum dolor sit amet, consectetur adipiscing elit, sed do eiusmod tempor incididunt ut labore et dolore magna aliqua. Ut enim ad minim veniam.</p>
    <nav class="tabbar">
      <div class="tab is-active"><svg viewBox="0 0 22 20"><circle cx="11" cy="10" r="8" fill="#fff"/></svg>Home</div>
      <div class="tab"><svg viewBox="0 0 22 20"><path d="M2 9 L20 6" stroke="#fff" stroke-width="2"/><path d="M11 8 L7 16 H15 Z" fill="#fff"/></svg>Imbalance</div>
      <div class="tab"><svg viewBox="0 0 22 20"><path d="M6 10 L16 4 M6 10 L16 16" stroke="#fff" stroke-width="2"/><circle cx="6" cy="10" r="3.5" fill="#fff"/><circle cx="16" cy="4" r="3.5" fill="#fff"/><circle cx="16" cy="16" r="3.5" fill="#fff"/></svg>Share</div>
      <div class="tab"><svg viewBox="0 0 22 20"><circle cx="11" cy="10" r="8.5" fill="none" stroke="#fff" stroke-width="1.5"/><rect x="10" y="8.5" width="2" height="6.5" fill="#fff"/><circle cx="11" cy="6" r="1.2" fill="#fff"/></svg>Info</div>
    </nav>
  </section>

  <section class="screen ailment">
    <div class="hero" role="img" aria-label="Video still of a smiling instructor, with a play button"></div>
    <svg class="hero__play" width="36" height="40" viewBox="0 0 36 40"><path d="M4 4 L32 20 L4 36 Z" fill="none" stroke="var(--orange)" stroke-width="3" stroke-linejoin="round"/></svg>
    <h1 class="title">Ear Pain</h1>
    <div class="rule"></div>
    <p class="body">Lorem ipsum dolor sit amet, consectetur adipiscing elit, sed do eiusmod tempor incididunt ut labore et dolore magna aliqua. Ut enim ad minim veniam. Lorem ipsum dolor sit amet, consectetur adipiscing elit, sed do eiusmod tempor incididunt ut labore et dolore magna aliqua. Ut enim ad minim veniam.</p>
    <nav class="tabbar">
      <div class="tab"><svg viewBox="0 0 22 20"><circle cx="11" cy="10" r="8" fill="#fff"/></svg>Home</div>
      <div class="tab is-active"><svg viewBox="0 0 22 20"><path d="M2 9 L20 6" stroke="#fff" stroke-width="2"/><path d="M11 8 L7 16 H15 Z" fill="#fff"/></svg>Imbalance</div>
      <div class="tab"><svg viewBox="0 0 22 20"><path d="M6 10 L16 4 M6 10 L16 16" stroke="#fff" stroke-width="2"/><circle cx="6" cy="10" r="3.5" fill="#fff"/><circle cx="16" cy="4" r="3.5" fill="#fff"/><circle cx="16" cy="16" r="3.5" fill="#fff"/></svg>Share</div>
      <div class="tab"><svg viewBox="0 0 22 20"><circle cx="11" cy="10" r="8.5" fill="none" stroke="#fff" stroke-width="1.5"/><rect x="10" y="8.5" width="2" height="6.5" fill="#fff"/><circle cx="11" cy="6" r="1.2" fill="#fff"/></svg>Info</div>
    </nav>
  </section>

  <section class="screen screen--picker picker">
    <h1 class="picker__title">Ear Pain</h1>
    <div class="picker__rule"></div>
    <p class="picker__intro">There are multiple ways to help relieve your child's ear pain</p>
    <p class="picker__cta">Select a spot to get started</p>
    <div class="spots">
      <div class="spot spot--feet" role="img" aria-label="Photo of a baby's feet"><span>Feet</span></div>
      <div class="spot spot--hands" role="img" aria-label="Photo of a baby's hands"><span>Hands</span></div>
      <div class="spot spot--face" role="img" aria-label="Photo of a baby in a knitted hat"><span>Face</span></div>
      <div class="spot spot--body" role="img" aria-label="Photo of a baby's body, locked"><span>Body</span>
        <div class="lock"><svg width="8" height="10" viewBox="0 0 8 10"><path d="M2 4 V2.5 a2 2 0 0 1 4 0 V4" fill="none" stroke="var(--orange)" stroke-width="1"/><rect x="1" y="4" width="6" height="5" rx="1" fill="none" stroke="var(--orange)" stroke-width="1"/></svg></div>
      </div>
    </div>
    <div class="spot-center">Ear pain</div>
    <nav class="tabbar">
      <div class="tab"><svg viewBox="0 0 22 20"><circle cx="11" cy="10" r="8" fill="#fff"/></svg>Home</div>
      <div class="tab is-active"><svg viewBox="0 0 22 20"><path d="M2 9 L20 6" stroke="#fff" stroke-width="2"/><path d="M11 8 L7 16 H15 Z" fill="#fff"/></svg>Imbalance</div>
      <div class="tab"><svg viewBox="0 0 22 20"><path d="M6 10 L16 4 M6 10 L16 16" stroke="#fff" stroke-width="2"/><circle cx="6" cy="10" r="3.5" fill="#fff"/><circle cx="16" cy="4" r="3.5" fill="#fff"/><circle cx="16" cy="16" r="3.5" fill="#fff"/></svg>Share</div>
      <div class="tab"><svg viewBox="0 0 22 20"><circle cx="11" cy="10" r="8.5" fill="none" stroke="#fff" stroke-width="1.5"/><rect x="10" y="8.5" width="2" height="6.5" fill="#fff"/><circle cx="11" cy="6" r="1.2" fill="#fff"/></svg>Info</div>
    </nav>
  </section>

</main>
</body>
</html>
```